Christian author seeks a Christian book cover design (paperback and ebook)

The reoccurring image in my book is seen in the following sentences:
"They noticed a man walking down the street wearing a backpack. The hunched over man staggered arduously as he stumbled under its weight."
"They saw a man trudging along the sidewalk under the weight of a backpack strapped to his spine."
I would like this image to be captured on the cover. Because this man's struggle represents a universal plight, I don't want the man on the cover to be identified by any skin color, hair style, age, etc. Instead, I would like these features to be fully covered (e.g., he's wearing a sweatshirt with the hood covering his head and pants that fully cover his legs), or else a light silhouette of a man wearing a backpack (I don't want the silhouette to be too dark. A silhouette of the attached picture or something like it would be excellent. In addition, I would either like the man's back to be facing the cover or a side view of the man/silhouette. A light nature scene could fill the background (something like the cover of Warren Pellby's album "Hold the Lantern"), but that's up to the designer.
Updates

In addition to what I have posted, can the words "A Novel" be added in small font below the title?

Target Market(s)

Any Christians, and also non-Christians who are curious about Christianity

Font styles to use
Serif

Requirements
Must have
• The cover must have the title (Burdened Passage) and my name (Martin K. Abernoy). It also must have the words A Novel in small letters below the title.
Nice to have
• I would like the book title to be at the top half of the cover and my name to be in smaller font at the bottom third or quarter of the cover.

```html
<!DOCTYPE html>
<html lang="en">
<head>
<meta charset="utf-8">
<title>Burdened Passage — A Novel — Martin K. Abernoy</title>
<link rel="stylesheet" href="https://fonts.googleapis.com/css2?family=Anton&family=Josefin+Sans:wght@400;600&display=swap">
<style>
  :root {
    --page-bg: #ececec;
    --sky-top: #c7b294;
    --sky-mid: #e6d9bb;
    --sky-low: #efe6d2;
    --sky-glow: #fffcf4;
    --sky-edge: #d8c49f;
    --ground: #0a0705;
    --ground-warm: #2b1c0d;
    --figure: #16110c;
    --ink: #0d0d0d;
    --accent: #e05a0b;
    --accent-soft: #ec9466;
  }
  * { margin: 0; padding: 0; box-sizing: border-box; }
  html, body {
    width: 1200px;
    height: 853px;
    overflow: hidden;
    background: var(--page-bg);
  }
  .canvas {
    position: relative;
    width: 1200px;
    height: 853px;
  }
  .cover {
    position: absolute;
    left: 337px;
    top: 26px;
    width: 526px;
    height: 800px;
    overflow: hidden;
    box-shadow: 0 8px 24px rgba(0, 0, 0, 0.18);
  }
  .cover-sky {
    position: absolute;
    inset: 0;
    background:
      radial-gradient(ellipse 50% 30% at 22% 60%, var(--sky-glow) 0%, rgba(255, 252, 244, 0) 100%),
      linear-gradient(90deg, rgba(255, 255, 255, 0) 55%, rgba(200, 176, 140, 0.35) 100%),
      linear-gradient(180deg, var(--sky-top) 0%, var(--sky-mid) 30%, var(--sky-low) 55%, var(--sky-edge) 78%);
  }
  .cover-ground {
    position: absolute;
    left: 0;
    top: 0;
    width: 526px;
    height: 800px;
  }
  .cover-figure {
    position: absolute;
    left: 312px;
    top: 396px;
    width: 122px;
    height: 204px;
    border-radius: 46% 46% 30% 30% / 30% 30% 14% 14%;
    background: radial-gradient(ellipse 60% 55% at 55% 45%, var(--figure) 0%, rgba(22, 17, 12, 0.85) 60%, rgba(22, 17, 12, 0) 100%);
  }
  .title-block {
    position: absolute;
    left: 93px;
    top: 80px;
    width: 348px;
    text-align: center;
  }
  .title-top {
    display: block;
    font-family: "Josefin Sans", sans-serif;
    font-weight: 600;
    font-size: 44px;
    line-height: 40px;
    letter-spacing: 0.31em;
    margin-right: -0.31em;
    color: var(--ink);
  }
  .title-main {
    display: block;
    margin-top: 6px;
    height: 116px;
    font-family: "Anton", sans-serif;
    font-size: 90px;
    line-height: 90px;
    letter-spacing: 0.01em;
    transform: scale(1.14, 1.3);
    transform-origin: top center;
    background: linear-gradient(180deg, var(--accent) 0%, var(--accent) 55%, var(--accent-soft) 85%, rgba(236, 148, 102, 0.45) 100%);
    -webkit-background-clip: text;
    background-clip: text;
    -webkit-text-fill-color: transparent;
  }
  .subtitle {
    display: flex;
    align-items: center;
    justify-content: space-between;
    margin-top: 20px;
  }
  .subtitle-rule {
    width: 74px;
    height: 1.5px;
    background: var(--ink);
  }
  .subtitle-text {
    font-family: "Josefin Sans", sans-serif;
    font-weight: 600;
    font-size: 20px;
    letter-spacing: 0.5em;
    margin-right: -0.5em;
    color: var(--ink);
  }
  .author {
    position: absolute;
    left: 0;
    right: 0;
    top: 700px;
    text-align: center;
    font-family: "Josefin Sans", sans-serif;
    font-weight: 600;
    font-size: 20px;
    letter-spacing: 0.26em;
    margin-right: -0.26em;
    color: var(--accent);
  }
</style>
</head>
<body>
  <main class="canvas">
    <article class="cover">
      <div class="cover-sky" role="img" aria-label="Photograph: warm hazy sunset sky glowing low on the left"></div>
      <svg class="cover-ground" viewBox="0 0 526 800" aria-hidden="true">
        <defs>
          <linearGradient id="groundShade" x1="0" y1="0" x2="0" y2="1">
            <stop offset="0" stop-color="#2b1c0d"/>
            <stop offset="0.12" stop-color="#0a0705"/>
            <stop offset="1" stop-color="#0a0705"/>
          </linearGradient>
        </defs>
        <path d="M0 545 C40 558 80 572 138 574 C230 578 300 596 360 600 C420 604 480 602 526 604 L526 800 L0 800 Z" fill="url(#groundShade)"/>
      </svg>
      <div class="cover-figure" role="img" aria-label="Photograph: silhouette of a hiker bent under a large backpack, walking on the hilltop"></div>
      <header class="title-block">
        <h1>
          <span class="title-top">BURDENED</span>
          <span class="title-main">PASSAGE</span>
        </h1>
        <p class="subtitle">
          <span class="subtitle-rule"></span>
          <span class="subtitle-text">A NOVEL</span>
          <span class="subtitle-rule"></span>
        </p>
      </header>
      <p class="author">MARTIN K. ABERNOY</p>
    </article>
  </main>
</body>
</html>
```